TECH PROJECT NEEDS NEW SKINS FOR RE-BRANDING

We are a technology project that has a product (crypto wallet) nearing release, have basic designs made so far however we need NEW SKINS/ branding/ design options for this wallet to change the look and feel -- it will be called and re-branded as "KESTRIL" a futuristic/ space/ edgy product so need it to look like so.

YOU ARE ALLOWED TO CHANGE + EXPERIMENT WITH THE LAYOUT/ schema and UI as you see fit -- (we are open to new and creative ideas)

(see WALLET.PNG and PROTFOLIO.PNG ATTACHED --- these are the pages we need new skins for )

(see KESTRIL logo attached --- PLEASE USE THIS LOGO/ VERSIONS OF THIS LOGO IN YOUR DESIGNS/SKIN SUBMISSIONS -- WE PROVIDED THE ai file so feel free to alter the logo a bit to experiment if you want -- we are open and flexible to new creative ideas)

(FOR A MOOD BOARD FOR GUIDANCE on feel/colors/mood-- SEE "SAMPLE INTERFACE 1 & 2" ATTACHED)

Target Market(s)

TECHNOLOGY/SPACE/ FUTURE

Number of Pages Required

2 page

Colors

Designer to choose colors to be used in the design.

Requirements
Must have
• MUST USE OUR KESTRIL LOGO OR A SIMILAR ALTERATION OF IT

```html
<!DOCTYPE html>
<html lang="en">
<head>
<meta charset="utf-8">
<title>KESTRIL Wallet</title>
<link rel="stylesheet" href="https://fonts.googleapis.com/css2?family=Montserrat:wght@300;400;500;600;700&display=swap">
<style>
:root{
  --rail:#10597a;
  --panel:#0f5574;
  --main:#0b4a66;
  --band:#17698b;
  --active:#1d86ad;
  --line:rgba(120,200,230,.12);
  --text:#ffffff;
  --muted:#bfe3f0;
  --yellow:#f5d31c;
  --send:#f28a5c;
  --recv:#6fe27c;
  --cyan:#4fe3f0;
  --btn:#1f8fb8;
  --btn-edge:#5fd3f0;
}
*{box-sizing:border-box;margin:0;padding:0}
html,body{width:1200px;height:675px;overflow:hidden;background:var(--main)}
body{font-family:"Montserrat",sans-serif;color:var(--text);position:relative}
.grid{position:absolute;inset:0;background:
  repeating-linear-gradient(0deg,var(--line) 0 1px,transparent 1px 20px),
  repeating-linear-gradient(90deg,var(--line) 0 1px,transparent 1px 20px),var(--main)}
.rail{position:absolute;left:0;top:0;width:75px;height:675px;background:var(--rail)}
.brand{position:absolute;left:0;top:28px;width:75px;text-align:center}
.brand-dot{width:24px;height:24px;border-radius:50%;border:2px solid var(--cyan);margin:0 auto 6px}
.brand-name{font-size:12px;font-weight:600;color:var(--cyan);letter-spacing:1px}
.nav-item{position:absolute;left:0;width:75px;text-align:center;font-size:8.5px;color:var(--muted)}
.nav-item svg{display:block;margin:0 auto 3px}
.nav-item.active{background:var(--active);color:var(--yellow);height:56px;padding-top:13px;border-right:2px solid var(--cyan)}
.list{position:absolute;left:75px;top:0;width:206px;height:675px;background:var(--panel)}
.list h1{position:absolute;left:19px;top:32px;font-size:26px;font-weight:600}
.list .sub{position:absolute;left:19px;top:64px;font-size:8px;color:var(--muted)}
.field{position:absolute;border:1px solid rgba(95,211,240,.45);background:rgba(30,120,160,.35);font-size:9px;color:#e6f6fb;padding-left:9px;display:flex;align-items:center}
.field svg{position:absolute;right:6px}
.wallet{position:absolute;left:1px;width:204px;height:37px}
.wallet.active{background:var(--active)}
.coin{position:absolute;left:17px;top:8px;width:20px;height:20px;border-radius:50%;border:1.5px solid rgba(255,255,255,.5)}
.wallet .name{position:absolute;left:56px;top:5px;font-size:12.5px;font-weight:500}
.wallet .amt{position:absolute;left:56px;top:21px;font-size:8px;color:var(--muted);letter-spacing:.5px}
.wallet.active .amt{color:var(--yellow)}
.head-coin{position:absolute;left:318px;top:27px;width:38px;height:38px;border-radius:50%;background:#1b8bb3;border:2px solid var(--cyan)}
.title{position:absolute;left:366px;top:30px;font-size:26px;font-weight:600}
.rate{position:absolute;right:38px;top:37px;font-size:14.5px;font-weight:500;color:var(--yellow)}
.label{position:absolute;font-size:9px;color:var(--yellow);font-weight:500}
.balance{position:absolute;left:318px;top:97px;font-size:26px;font-weight:300;letter-spacing:.5px}
.fiat{position:absolute;left:318px;top:127px;font-size:14px;font-weight:300;letter-spacing:1px}
.address{position:absolute;left:318px;top:178px;font-size:8.6px;color:#e6f6fb;width:196px;white-space:nowrap;overflow:hidden}
.btn{position:absolute;height:26px;background:var(--btn);border:1px solid var(--btn-edge);font-size:9px;font-weight:500;display:flex;align-items:center;justify-content:center;gap:6px}
.thead{position:absolute;top:238px;font-size:8.5px;color:var(--muted);letter-spacing:.3px}
.row{position:absolute;left:300px;width:882px;height:37.6px;font-size:9px;font-weight:500}
.row.band{background:var(--band)}
.row span{position:absolute;top:14px}
.row svg{position:absolute;left:18px;top:11px}
.c-act{left:37px}.c-date{left:158px;letter-spacing:.5px}.c-id{left:262px;letter-spacing:.3px}
.c-amt{left:488px}.c-st{left:600px;color:var(--cyan)}.c-st.pending{color:var(--yellow)}
.c-bal{left:693px}.c-det{left:824px}
</style>
</head>
<body>
<svg width="0" height="0" style="position:absolute">
  <defs>
    <symbol id="i-send" viewBox="0 0 16 16"><path d="M5 3.5A6 6 0 1 0 11 3.5" fill="none" stroke="currentColor" stroke-width="1.6"/><path d="M8 9V1.5M5.5 4L8 1.5 10.5 4" fill="none" stroke="currentColor" stroke-width="1.6"/></symbol>
    <symbol id="i-recv" viewBox="0 0 16 16"><circle cx="8" cy="8" r="6.5" fill="none" stroke="currentColor" stroke-width="1.6"/><path d="M8 3.5V11M5.5 8.5L8 11l2.5-2.5" fill="none" stroke="currentColor" stroke-width="1.6"/></symbol>
    <symbol id="i-search" viewBox="0 0 16 16"><circle cx="6.5" cy="6.5" r="5" fill="none" stroke="currentColor" stroke-width="1.6"/><path d="M10.5 10.5L15 15" stroke="currentColor" stroke-width="1.8"/></symbol>
  </defs>
</svg>
<div class="grid"></div>

<nav class="rail">
  <div class="brand"><div class="brand-dot"></div><div class="brand-name">KESTRIL</div></div>
  <div class="nav-item" style="top:145px"><svg width="16" height="16" style="color:#dff"><use href="#i-recv"/></svg>Dashboard</div>
  <div class="nav-item" style="top:201px"><svg width="16" height="16"><circle cx="8" cy="8" r="7" fill="none" stroke="#dff" stroke-width="1.6"/><circle cx="8" cy="6" r="2.5" fill="#dff"/></svg>Portfolio</div>
  <div class="nav-item active" style="top:244px"><svg width="16" height="14"><rect x="1" y="2" width="14" height="11" rx="3" fill="#fff"/></svg>Wallets</div>
  <div class="nav-item" style="top:313px"><svg width="18" height="14"><path d="M4 11a3.5 3.5 0 0 1 1-7 4.5 4.5 0 0 1 8.5 1A3 3 0 0 1 14 11z" fill="#dff"/></svg>Lightning</div>
  <div class="nav-item" style="top:370px"><svg width="18" height="14"><path d="M4 11a3.5 3.5 0 0 1 1-7 4.5 4.5 0 0 1 8.5 1A3 3 0 0 1 14 11z" fill="none" stroke="#dff" stroke-width="1.4"/></svg>SND Cloud</div>
  <div class="nav-item" style="top:632px"><svg width="18" height="16"><path d="M2 4h14M2 8h14M2 12h14" stroke="#dff" stroke-width="1.4"/><path d="M11 2v4M6 6v4M12 10v4" stroke="#dff" stroke-width="1.6"/></svg>Settings</div>
</nav>

<aside class="list">
  <h1>Wallets</h1>
  <div class="sub">6 Active Wallets</div>
  <div class="field" style="left:20px;top:94px;width:166px;height:27px">Search<svg width="14" height="14" style="color:var(--cyan)"><use href="#i-search"/></svg></div>
  <div class="wallet" style="top:141px"><div class="coin" style="background:#b8533a"></div><div class="name">Orbicoin-ORB</div><div class="amt">10.21000192 ORB</div></div>
  <div class="wallet" style="top:178px"><div class="coin" style="background:#2f7fbf"></div><div class="name">Dartcoin-DRT</div><div class="amt">30.51 DRT</div></div>
  <div class="wallet" style="top:216px"><div class="coin" style="background:#7a4fbf"></div><div class="name">Aetheron-AET</div><div class="amt">1.100.00 AET</div></div>
  <div class="wallet" style="top:253px"><div class="coin" style="background:#a9416f"></div><div class="name">Lumecoin-LMC</div><div class="amt">961.005 LMC</div></div>
  <div class="wallet" style="top:291px"><div class="coin" style="background:#2fa56a"></div><div class="name">Wavelet-WVL</div><div class="amt">210.0176 WVL</div></div>
  <div class="wallet active" style="top:329px"><div class="coin" style="background:#2e4f9c"></div><div class="name">Starnode-SND</div><div class="amt">369.800.00 SND</div></div>
</aside>

<main>
  <div class="head-coin"></div>
  <div class="title">Starnode-SND</div>
  <div class="rate">1.00 SND = 0.08 USD</div>
  <div class="label" style="left:318px;top:85px">Balance</div>
  <div class="balance">369.800.00 SND</div>
  <div class="fiat">= 29.584.00 USD</div>
  <div class="label" style="left:318px;top:160px">Wallet Address</div>
  <div class="address">Ktr4qW7mLx9NvBzP2aHcR8sYdFe6GjU3oW</div>
  <div class="btn" style="left:526px;top:170px;width:64px;height:25px"><svg width="10" height="12"><rect x="1" y="1" width="8" height="10" rx="1.5" fill="none" stroke="#fff" stroke-width="1.2"/></svg>Copy</div>
  <div class="btn" style="left:929px;top:104px;width:110px"><svg width="13" height="13" style="color:#fff"><use href="#i-send"/></svg>Send Money</div>
  <div class="btn" style="left:1050px;top:104px;width:112px"><svg width="13" height="13" style="color:#fff"><use href="#i-recv"/></svg>Receive Money</div>
  <div class="field" style="left:929px;top:170px;width:232px;height:25px">Search Transactions<svg width="14" height="14" style="color:var(--cyan)"><use href="#i-search"/></svg></div>

  <div class="thead" style="left:318px">ACTIVITY</div>
  <div class="thead" style="left:458px">DATE</div>
  <div class="thead" style="left:562px">TRANSACTIONS ID</div>
  <div class="thead" style="left:788px">AMOUNT</div>
  <div class="thead" style="left:900px">STATUS</div>
  <div class="thead" style="left:993px">BALANCE CHANGE</div>
  <div class="thead" style="left:1124px">DETAILS</div>

  <div class="row band" style="top:263px"><svg width="13" height="13" style="color:var(--send)"><use href="#i-send"/></svg><span class="c-act">Sending Money</span><span class="c-date">15 Feb 2019</span><span class="c-id">a3f19e2bc84d07e5f6a21c9d830b4...</span><span class="c-amt">2019.82 SND</span><span class="c-st pending">Pending</span><span class="c-bal">369.800.00 SND</span><span class="c-det">Details</span></div>
  <div class="row" style="top:300.6px"><svg width="13" height="13" style="color:var(--recv)"><use href="#i-recv"/></svg><span class="c-act">Money Received</span><span class="c-date">14 Feb 2019</span><span class="c-id">4e8d2f0b7ac13e96d5b08f2c4a17e...</span><span class="c-amt">2700.00 SND</span><span class="c-st">Success</span><span class="c-bal">369.800.00 SND</span><span class="c-det">Details</span></div>
  <div class="row band" style="top:338.2px"><svg width="13" height="13" style="color:var(--send)"><use href="#i-send"/></svg><span class="c-act">Sending Money</span><span class="c-date">14 Feb 2019</span><span class="c-id">a3f19e2bc84d07e5f6a21c9d830b4...</span><span class="c-amt">49.20 SND</span><span class="c-st">Success</span><span class="c-bal">369.800.00 SND</span><span class="c-det">Details</span></div>
  <div class="row" style="top:375.8px"><svg width="13" height="13" style="color:var(--recv)"><use href="#i-recv"/></svg><span class="c-act">Money Received</span><span class="c-date">14 Feb 2019</span><span class="c-id">4e8d2f0b7ac13e96d5b08f2c4a17e...</span><span class="c-amt">132.85 SND</span><span class="c-st">Success</span><span class="c-bal">369.800.00 SND</span><span class="c-det">Details</span></div>
  <div class="row band" style="top:413.4px"><svg width="13" height="13" style="color:var(--send)"><use href="#i-send"/></svg><span class="c-act">Sending Money</span><span class="c-date">14 Feb 2019</span><span class="c-id">a3f19e2bc84d07e5f6a21c9d830b4...</span><span class="c-amt">49.20 SND</span><span class="c-st">Success</span><span class="c-bal">369.800.00 SND</span><span class="c-det">Details</span></div>
  <div class="row" style="top:451px"><svg width="13" height="13" style="color:var(--recv)"><use href="#i-recv"/></svg><span class="c-act">Money Received</span><span class="c-date">14 Feb 2019</span><span class="c-id">4e8d2f0b7ac13e96d5b08f2c4a17e...</span><span class="c-amt">132.85 SND</span><span class="c-st">Success</span><span class="c-bal">369.800.00 SND</span><span class="c-det">Details</span></div>
  <div class="row band" style="top:488.6px"><svg width="13" height="13" style="color:var(--send)"><use href="#i-send"/></svg><span class="c-act">Sending Money</span><span class="c-date">14 Feb 2019</span><span class="c-id">a3f19e2bc84d07e5f6a21c9d830b4...</span><span class="c-amt">49.20 SND</span><span class="c-st">Success</span><span class="c-bal">369.800.00 SND</span><span class="c-det">Details</span></div>
  <div class="row" style="top:526.2px"><svg width="13" height="13" style="color:var(--recv)"><use href="#i-recv"/></svg><span class="c-act">Money Received</span><span class="c-date">14 Feb 2019</span><span class="c-id">4e8d2f0b7ac13e96d5b08f2c4a17e...</span><span class="c-amt">132.85 SND</span><span class="c-st">Success</span><span class="c-bal">369.800.00 SND</span><span class="c-det">Details</span></div>
  <div class="row band" style="top:563.8px"><svg width="13" height="13" style="color:var(--send)"><use href="#i-send"/></svg><span class="c-act">Sending Money</span><span class="c-date">14 Feb 2019</span><span class="c-id">a3f19e2bc84d07e5f6a21c9d830b4...</span><span class="c-amt">49.20 SND</span><span class="c-st">Success</span><span class="c-bal">369.800.00 SND</span><span class="c-det">Details</span></div>
  <div class="row" style="top:601.4px"><svg width="13" height="13" style="color:var(--recv)"><use href="#i-recv"/></svg><span class="c-act">Money Received</span><span class="c-date">14 Feb 2019</span><span class="c-id">4e8d2f0b7ac13e96d5b08f2c4a17e...</span><span class="c-amt">132.85 SND</span><span class="c-st">Success</span><span class="c-bal">369.800.00 SND</span><span class="c-det">Details</span></div>
  <div class="row band" style="top:639px"><svg width="13" height="13" style="color:var(--send)"><use href="#i-send"/></svg><span class="c-act">Sending Money</span><span class="c-date">14 Feb 2019</span><span class="c-id">a3f19e2bc84d07e5f6a21c9d830b4...</span><span class="c-amt">49.20 SND</span><span class="c-st">Success</span><span class="c-bal">369.800.00 SND</span><span class="c-det">Details</span></div>
</main>
</body>
</html>
```